Business Card Design for Event Planning Company

Create a business card for event planning company using our new logo. After I pick the design, I will need files made for 6 employees. Our company provides event design & logistics services as well as venue management. The font should be sans serif and complementary to the logo. I will need to know the name of the font selected for the final design. The phone numbers listed should be separated by "." not "-"

Address for the card
PO Box 318, Washington, DC 20019

Card One
Lorna Pettibone
lpettibone@galavoyant.com
202.481.7730

Card Two
Miriam Okonkwo
mokonkwo@galavoyant.com
202.556.2047

Card Three
Tessa Varnholt
tvarnholt@galavoyant.com
978.620.4471

Card Four
Robin Fess
rfess@galavoyant.com
202.718.3362

Card Five
Ada-Rose Pelletan-Uzor
adarose@galavoyant.com
202.839.1205

Card Six
Beatrix Holloway
Beatrix@galavoyant.com
202.492.6618

Target Market(s)

Corporate/Non-Profit

Industry/Entity Type

Event Planning

Contact Information for Business Card

Address for the card

Card One
Lorna Pettibone
lpettibone@galavoyant.com
202.481.7730

Card Two
Miriam Okonkwo
202.556.2047

Card Three
Tessa Varnholt
978.620.4471

Card Four
Robin Fess
rfess@galavoyant.com
202.718.3362

Card Five
Ada-Rose Pelletan-Uzor
202.839.1205

Card Six
Beatrix Holloway
202.492.6618

Font styles to use
Sans Serif

Colors

Designer to choose colors to be used in the design.

Requirements
Must have
• Two-sided with logo
Should not have
• Extra colors or be too busy

```html
<!DOCTYPE html>
<html lang="en">
<head>
<meta charset="utf-8">
<title>Galavoyant business cards</title>
<link rel="stylesheet" href="https://fonts.googleapis.com/css2?family=Source+Sans+3:wght@300;400&display=swap">
<style>
  :root {
    --teal: #5ea6a5;
    --teal-deep: #3f8584;
    --ink: #231f20;
    --paper: #ffffff;
    --rule: #c9c9c9;
  }
  * { box-sizing: border-box; margin: 0; padding: 0; }
  html, body { width: 1200px; height: 1200px; overflow: hidden; background: var(--paper); }
  body { position: relative; font-family: "Source Sans 3", sans-serif; color: var(--ink); }

  .card { position: absolute; width: 535px; height: 312px; overflow: hidden; }
  .front { left: 26px; background: var(--teal); }
  .back { left: 629px; background: var(--paper); border: 1px solid var(--rule); overflow: visible; }
  .row-1 { top: 59px; }
  .row-2 { top: 426px; }
  .row-3 { top: 798px; }

  /* front */
  .front .band {
    position: absolute; left: 0; top: 145px; width: 100%; height: 120px;
    background: var(--paper);
    box-shadow: 0 -6px 14px -6px rgba(30,70,70,.55), 0 6px 14px -6px rgba(30,70,70,.55);
  }
  .front .wordmark {
    position: absolute; left: 0; width: 100%; top: 44px; text-align: center;
    font-weight: 300; font-size: 38px; line-height: 1; letter-spacing: .5px; color: var(--ink);
  }
  .front .tagline {
    position: absolute; left: 0; width: 100%; top: 96px; text-align: center;
    font-size: 7.5px; letter-spacing: 5px; color: var(--ink);
  }
  .ornament-top {
    position: absolute; left: 14px; top: 8px; width: 196px; height: 137px;
    background: radial-gradient(ellipse at 45% 55%, rgba(255,255,255,.55), rgba(255,255,255,0) 70%);
  }
  .ornament-bottom {
    position: absolute; right: 0; bottom: 0; width: 193px; height: 47px;
    background: linear-gradient(100deg, rgba(255,255,255,0) 10%, rgba(255,255,255,.45) 60%, rgba(255,255,255,.2));
  }

  /* back */
  .back .bar-vertical { position: absolute; left: 255px; top: 0; width: 27px; height: 94px; background: var(--ink); }
  .back .bar-bottom { position: absolute; left: -1px; right: -3px; top: 289px; height: 23px; background: var(--ink); }
  .back .accent-square { position: absolute; left: 255px; top: 282px; width: 27px; height: 30px; background: var(--teal); }

  .contact { position: absolute; left: 28px; top: 0; list-style: none; }
  .contact li { position: absolute; left: 0; display: flex; align-items: center; white-space: nowrap; }
  .contact .icon { width: 21px; height: 21px; flex: none; }
  .contact .name { top: 98px; font-size: 21px; }
  .contact .name .icon { margin-right: 13px; }
  .contact .email { top: 128px; }
  .contact .phone { top: 163px; }
  .contact .address { top: 197px; }
  .contact .detail { font-size: 11.5px; }
  .contact .detail .icon { margin-right: 10px; }

  .back .wordmark {
    position: absolute; left: 402px; top: 162px; transform: translateX(-50%);
    font-weight: 300; font-size: 32px; line-height: 1; letter-spacing: .4px; color: var(--ink);
  }
</style>
</head>
<body>
<svg width="0" height="0" style="position:absolute" aria-hidden="true">
  <symbol id="icon-person" viewBox="0 0 20 20">
    <circle cx="10" cy="10" r="10" fill="#231f20"/>
    <circle cx="10" cy="7.4" r="3" fill="#fff"/>
    <path d="M4.8 15.2c.6-3 2.6-4.4 5.2-4.4s4.6 1.4 5.2 4.4z" fill="#fff"/>
  </symbol>
  <symbol id="icon-email" viewBox="0 0 20 20">
    <circle cx="10" cy="10" r="10" fill="#231f20"/>
    <circle cx="10" cy="10" r="6.2" fill="none" stroke="#fff" stroke-width="1.3"/>
    <circle cx="10" cy="10" r="3.6" fill="none" stroke="#fff" stroke-width="1.3"/>
    <circle cx="10" cy="10" r="1.3" fill="#fff"/>
  </symbol>
  <symbol id="icon-phone" viewBox="0 0 20 20">
    <circle cx="10" cy="10" r="10" fill="#231f20"/>
    <path d="M6.2 5.2l2 .1 1 2.6-1.3 1.1c.7 1.4 1.7 2.4 3.1 3.1l1.1-1.3 2.6 1 .1 2c-.1.6-.6 1-1.2 1-4.3-.3-7.6-3.6-7.9-7.9 0-.6.4-1.1 1-1.2z" fill="#fff"/>
  </symbol>
</svg>

<!-- Fronts -->
<section class="card front row-1">
  <div class="ornament-top" role="img" aria-label="White leafy floral flourish"></div>
  <div class="band">
    <div class="wordmark">galavoyant</div>
    <div class="tagline">EVENT PLANNERS</div>
  </div>
  <div class="ornament-bottom" role="img" aria-label="White swirling floral flourish"></div>
</section>
<section class="card front row-2">
  <div class="band">
    <div class="wordmark">galavoyant</div>
    <div class="tagline">EVENT PLANNERS</div>
  </div>
  <div class="ornament-bottom" role="img" aria-label="White swirling floral flourish"></div>
</section>
<section class="card front row-3">
  <div class="band">
    <div class="wordmark">galavoyant</div>
    <div class="tagline">EVENT PLANNERS</div>
  </div>
  <div class="ornament-bottom" role="img" aria-label="White swirling floral flourish"></div>
</section>

<!-- Backs -->
<section class="card back row-1">
  <div class="bar-vertical"></div>
  <ul class="contact">
    <li class="name"><svg class="icon"><use href="#icon-person"/></svg>Lorna Pettibone</li>
    <li class="detail email"><svg class="icon"><use href="#icon-email"/></svg>lpettibone@galavoyant.com</li>
    <li class="detail phone"><svg class="icon"><use href="#icon-phone"/></svg>202.481.7730</li>
    <li class="detail address"><svg class="icon"><use href="#icon-phone"/></svg>PO Box 318, Washington, DC 20019</li>
  </ul>
  <div class="wordmark">galavoyant</div>
  <div class="bar-bottom"></div>
  <div class="accent-square"></div>
</section>
<section class="card back row-2">
  <div class="bar-vertical"></div>
  <ul class="contact">
    <li class="name"><svg class="icon"><use href="#icon-person"/></svg>Miriam Okonkwo</li>
    <li class="detail email"><svg class="icon"><use href="#icon-email"/></svg>mokonkwo@galavoyant.com</li>
    <li class="detail phone"><svg class="icon"><use href="#icon-phone"/></svg>202.556.2047</li>
    <li class="detail address"><svg class="icon"><use href="#icon-phone"/></svg>PO Box 318, Washington, DC 20019</li>
  </ul>
  <div class="wordmark">galavoyant</div>
  <div class="bar-bottom"></div>
  <div class="accent-square"></div>
</section>
<section class="card back row-3">
  <ul class="contact">
    <li class="name"><svg class="icon"><use href="#icon-person"/></svg>Tessa Varnholt</li>
    <li class="detail email"><svg class="icon"><use href="#icon-email"/></svg>tvarnholt@galavoyant.com</li>
    <li class="detail phone"><svg class="icon"><use href="#icon-phone"/></svg>978.620.4471</li>
    <li class="detail address"><svg class="icon"><use href="#icon-phone"/></svg>PO Box 318, Washington, DC 20019</li>
  </ul>
  <div class="wordmark">galavoyant</div>
  <div class="bar-bottom"></div>
  <div class="accent-square"></div>
</section>
</body>
</html>
```